Plakat für Schaufenster
Zielgruppe
Moin Moin,
ich habe einen kleinen Fahrradladen in einem historischen Gebäude. Wir führen ein sehr hochwertiges und ausgesuchtes Programm diverser Hersteller und bieten eine umfassende individuelle Beratung
Aufgabenstellung
Ein Fahrradladen ist einerseits ein Handwerksbetrieb anderseits auch ein Handelsbetrieb. Da ich als Einzelkämpfer in meinem Laden arbeite, habe ich diese beiden Betriebe zeitlich voneinander getrennt. Ich arbeite Vormittags in der Werkstatt und Nachmitttags ist mein Laden für Service und Beratung geöffnet, d.h. meine Laden ist nur Nachmittags von 14-18 und Samstag von 10-13 Uhr geöffnet. Durch diese Regelung kann ich kurze Reparaturzeiten und gute Beratung bieten.
Leider denken nun viele Menschen wenn Sie Vormittags vor verschlossener Tür stehen: "der hat es nicht nötig und arbeitet nur noch halbe Tage!".
Nun möchte ich mit einem Plakat im Fenster meinen "geteilten" Betrieb bzw. meine Arbeitsteilung erklären.
Vielleicht in Form einer analogen Uhr mit entsprechender Teilung !?! Aber auch andere Ideen sind herzlich Willkommen !!

```html
<!DOCTYPE html>
<html lang="de">
<head>
<meta charset="utf-8">
<title>Plakat – Öffnungszeiten Fahrradladen</title>
<link rel="stylesheet" href="https://fonts.googleapis.com/css2?family=Fredoka:wght@600&display=swap">
<style>
  :root {
    --backdrop: #e6e4e1;
    --cream: #fbe7cf;
    --green: #0f5a22;
    --green-text: #1d6a30;
    --green-soft: #4f9a62;
    --red: #c8001e;
    --red-text: #f6dcc4;
    --ring: #8a8a8a;
    --bike-area: #ececec;
  }
  html, body {
    margin: 0;
    width: 1200px;
    height: 1148px;
    overflow: hidden;
    background: var(--backdrop);
  }
  .poster {
    position: absolute;
    left: 205px;
    top: 19px;
    width: 790px;
    height: 1110px;
    box-shadow: 0 6px 24px rgba(0,0,0,.18);
  }
  .poster svg { display: block; }
  .label {
    font-family: "Fredoka", "Arial Rounded MT Bold", sans-serif;
    font-weight: 600;
    text-anchor: middle;
    dominant-baseline: central;
  }
  .bg-cream { fill: var(--cream); }
  .bg-green { fill: var(--green); }
  .frame-dots { fill: none; stroke: var(--green); stroke-width: 2; stroke-dasharray: 2 4; }
  .wheel-ghost { fill: none; stroke: rgba(110,110,110,.28); stroke-width: 3; }
  .ribbon-shadow { fill: rgba(60,40,20,.28); }
  .ribbon-red { fill: var(--red); }
  .ribbon-cream { fill: var(--cream); }
  .text-red-small { fill: var(--red-text); font-size: 25px; }
  .text-red { fill: #fff6ee; font-size: 36px; }
  .text-green-soft { fill: var(--green-soft); font-size: 32px; }
  .text-green { fill: var(--green-text); font-size: 34px; }
  .badge-ring { fill: #fff; stroke: var(--ring); stroke-width: 8; }
  .badge-dots { fill: none; stroke: var(--green); stroke-width: 2; stroke-dasharray: 2 4; }
  .bike-illustration { fill: var(--bike-area); }
</style>
</head>
<body>
<div class="poster">
  <svg width="790" height="1110" viewBox="0 0 790 1110">
    <rect class="bg-cream" x="0" y="0" width="790" height="560"/>
    <rect class="bg-green" x="0" y="560" width="790" height="550"/>
    <rect class="frame-dots" x="34" y="34" width="722" height="1042"/>

    <circle class="wheel-ghost" cx="395" cy="560" r="300"/>

    <!-- Öffnungszeiten -->
    <g class="ribbon" transform="rotate(-6 395 160)">
      <polygon class="ribbon-shadow" points="203,128 623,128 603,168 623,208 203,208"/>
      <polygon class="ribbon-red" points="195,120 615,120 595,160 615,200 195,200"/>
      <text class="label text-red-small" x="395" y="160">PERSÖNLICHE BERATUNG:</text>
    </g>
    <g class="ribbon" transform="rotate(-6 400 265)">
      <rect class="ribbon-shadow" x="208" y="228" width="400" height="90"/>
      <rect class="ribbon-red" x="200" y="220" width="400" height="90"/>
      <text class="label text-red" x="400" y="265">MO-FR VON 14-18 UHR</text>
    </g>
    <g class="ribbon" transform="rotate(-6 395 372)">
      <polygon class="ribbon-shadow" points="193,335 613,335 613,425 193,425 213,380"/>
      <polygon class="ribbon-red" points="185,327 605,327 605,417 185,417 205,372"/>
      <text class="label text-red" x="405" y="372">SA VON 10-13 UHR</text>
    </g>

    <!-- Mittiges Emblem -->
    <circle class="badge-ring" cx="395" cy="560" r="106"/>
    <circle class="bike-illustration" cx="395" cy="560" r="86" role="img" aria-label="Illustration eines historischen Fahrrads"/>
    <circle class="badge-dots" cx="395" cy="560" r="92"/>

    <!-- Werkstattzeiten -->
    <g class="ribbon" transform="rotate(-6 400 735)">
      <polygon class="ribbon-shadow" points="208,702 628,702 608,742 628,782 208,782"/>
      <polygon class="ribbon-cream" points="200,694 620,694 600,735 620,776 200,776"/>
      <text class="label text-green-soft" x="400" y="735">VORMITTAGS:</text>
    </g>
    <g class="ribbon" transform="rotate(-6 405 845)">
      <rect class="ribbon-shadow" x="213" y="808" width="400" height="90"/>
      <rect class="ribbon-cream" x="205" y="800" width="400" height="90"/>
      <text class="label text-green" x="405" y="845">REPARATURARBEITEN</text>
    </g>
    <g class="ribbon" transform="rotate(-6 400 955)">
      <polygon class="ribbon-shadow" points="198,918 618,918 618,1008 198,1008 218,963"/>
      <polygon class="ribbon-cream" points="190,910 610,910 610,1000 190,1000 210,955"/>
      <text class="label text-green" x="410" y="955">IN DER WERKSTATT!</text>
    </g>
  </svg>
</div>
</body>
</html>
```